Startup Drone Platform Company business card

We are needing a business card design for our employees. We are a startup drone platform. We are looking for a business card that has our logo on one side, with the employee/company details on the opposite side. We are looking for something that is very eye catching, modern, and bold.

Target Market(s)

This will target both drone pilots and drone businesses, along with all the industries that could utilize drone services (aerial video, aerial photos, inspections, 3d mapping, etc).

Industry/Entity Type

Business

```html
<!DOCTYPE html>
<html lang="en">
<head>
<meta charset="utf-8">
<title>Nimbrel Aerial – Business Card</title>
<link rel="stylesheet" href="https://fonts.googleapis.com/css2?family=Montserrat:wght@500&family=Rajdhani:wght@500&family=Arimo:wght@400&display=swap">
<style>
  :root {
    --backdrop: #6b6b6b;
    --card-white: #fbfbfb;
    --teal: #5fc3ca;
    --white: #ffffff;
  }
  * { margin: 0; padding: 0; box-sizing: border-box; }
  html, body { width: 1200px; height: 867px; overflow: hidden; }
  body { background: var(--backdrop); position: relative; }

  .card { position: absolute; height: 428px; overflow: hidden; }

  .brand { position: absolute; display: flex; flex-direction: column; align-items: center; }
  .brand-dot { border-radius: 50%; border: 4px solid currentColor; }
  .brand-name {
    font-family: "Montserrat", sans-serif; font-weight: 500;
    text-transform: uppercase; text-align: center; white-space: nowrap;
  }
  .brand-line { display: block; }

  /* Front: contact side */
  .card-front { left: 33px; top: 29px; width: 795px; background: var(--card-white); z-index: 1; }
  .card-front .brand { left: 66px; width: 260px; top: 88px; color: var(--teal); }
  .card-front .brand-dot { width: 120px; height: 120px; margin-bottom: 62px; }
  .card-front .brand-line-main { font-size: 24px; line-height: 32px; letter-spacing: 0.35em; padding-left: 0.35em; }
  .card-front .brand-line-sub { font-size: 17px; line-height: 30px; letter-spacing: 0.3em; padding-left: 0.3em; }

  .front-rule { position: absolute; left: 96px; width: 198px; top: 376px; height: 3px; background: var(--teal); }
  .front-block { position: absolute; left: 96px; width: 198px; top: 384px; height: 44px; background: var(--teal); }

  .holder { position: absolute; left: 424px; top: 80px; color: var(--teal); }
  .holder-name { font-family: "Rajdhani", sans-serif; font-weight: 500; font-size: 34px; line-height: 1; }
  .holder-title { font-family: "Arimo", sans-serif; font-size: 11.5px; margin-top: 2px; letter-spacing: 0.02em; }

  .contacts { position: absolute; left: 424px; top: 206px; list-style: none; color: var(--teal); }
  .contacts li {
    display: flex; align-items: flex-start; gap: 20px;
    font-family: "Arimo", sans-serif; font-size: 15.5px; line-height: 20px;
    margin-bottom: 9px; letter-spacing: 0.01em;
  }
  .contacts svg { width: 18px; height: 18px; flex: none; margin-top: 1px; }

  /* Back: brand side */
  .card-back { left: 369px; top: 397px; width: 792px; height: 430px; background: var(--teal); z-index: 2; color: var(--white); }
  .card-back .brand { left: 0; right: 0; top: 95px; }
  .card-back .brand-dot { width: 150px; height: 150px; margin-bottom: 40px; }
  .card-back .brand-line-main { font-size: 27px; line-height: 36px; letter-spacing: 0.35em; padding-left: 0.35em; }
  .card-back .brand-line-sub { font-size: 20px; line-height: 36px; letter-spacing: 0.3em; padding-left: 0.3em; }

  .back-footer {
    position: absolute; left: 0; right: 0; top: 396px;
    display: flex; align-items: center; gap: 12px;
  }
  .back-footer::before, .back-footer::after { content: ""; flex: 1; height: 1px; background: rgba(255,255,255,0.8); }
  .back-url { font-family: "Arimo", sans-serif; font-size: 10px; letter-spacing: 0.22em; color: var(--white); }
</style>
</head>
<body>

<section class="card card-front">
  <div class="brand">
    <div class="brand-dot"></div>
    <p class="brand-name"><span class="brand-line brand-line-main">Nimbrel</span><span class="brand-line brand-line-sub">Aerial</span></p>
  </div>
  <div class="front-rule"></div>
  <div class="front-block"></div>

  <div class="holder">
    <h1 class="holder-name">Martin Calloway</h1>
    <p class="holder-title">Managing Director</p>
  </div>

  <ul class="contacts">
    <li>
      <svg viewBox="0 0 18 18" fill="none" stroke="currentColor" stroke-width="1.4"><circle cx="9" cy="9" r="7.5"/><ellipse cx="9" cy="9" rx="3.2" ry="7.5"/><path d="M1.5 9h15M3 5h12M3 13h12"/></svg>
      <span>www.nimbrelaerial.com</span>
    </li>
    <li>
      <svg viewBox="0 0 18 18"><rect x="1" y="3.5" width="16" height="11" fill="currentColor"/><path d="M1.5 4l7.5 6 7.5-6" fill="none" stroke="#fbfbfb" stroke-width="1.3"/></svg>
      <span>Nimbrelaerial.net</span>
    </li>
    <li>
      <svg viewBox="0 0 18 18" fill="currentColor"><path d="M1 7c0-2 3-3.5 8-3.5S17 5 17 7v1.5h-4V7H5v1.5H1z"/><path d="M4 10h10l1.5 5h-13z"/></svg>
      <span>+1(555) 210-7789</span>
    </li>
    <li>
      <svg viewBox="0 0 18 18"><path d="M9 1a5.5 5.5 0 0 0-5.5 5.5C3.5 11 9 17 9 17s5.5-6 5.5-10.5A5.5 5.5 0 0 0 9 1z" fill="currentColor"/><circle cx="9" cy="6.5" r="2" fill="#fbfbfb"/></svg>
      <span>M4B 2K9 ON Harbour Street<br>Elmwood, Dr.</span>
    </li>
  </ul>
</section>

<section class="card card-back">
  <div class="brand">
    <div class="brand-dot"></div>
    <p class="brand-name"><span class="brand-line brand-line-main">Nimbrel</span><span class="brand-line brand-line-sub">Aerial</span></p>
  </div>
  <div class="back-footer">
    <span class="back-url">www.nimbrelaerial.com</span>
  </div>
</section>

</body>
</html>
```